BRACKENDALE FARM - TOP QUALITY HAY, STRAW AND HAYLAGE

we need an A5 flyer to promote/sell the hay, straw and haylage we produce on our farm. The hay and haylage is for horse feed/fodder and the straw is for horse bedding. We provide meadow and seed hay in small and large bales, and haylage in bale size 1.2 x 0.8 x 0.7m/165-175kgs. Oat and wheat straw is also available in small and large bales and barley straw in large bales. We are tempted not to quote prices but possible offer 10% discount on the 1st order/with this leaflet.We deliver to our customer yard and our policy is to provide our customers with consistent quality and a reliable service for as long as they require our product. In slightly smaller writing I would like a note 'we also sell home grown white marfona and red Mozart potatoes 12.5 and 25kg bags. Superb value for money at £3 and £5 per bag and they are delicious!We have a face book page /Brackendale Farm Barkby Thorpe and web site (to follow).contact details are Dennis Pell 07721379713Our branding is very dark green back ground with cream/gold lettering (see attached files) but I am happy for you to deviate from this if you think it would be more appropriate for example to have a straw back ground?
Target Market(s)
Horse owners, livery yards, riding schools, event yards, hunt yards
Industry/Entity Type
Farming
Other font styles liked:
- see lettering on attached file and use if you feel it is appropriate.

```html
<!DOCTYPE html>
<html lang="en">
<head>
<meta charset="utf-8">
<title>Brackendale Farm – Hay, Straw, Haylage</title>
<link href="https://fonts.googleapis.com/css2?family=Anton&family=Open+Sans:wght@600;700;800&display=swap" rel="stylesheet">
<style>
  :root {
    --green: #1f5b22;
    --green-dark: #0f3a14;
    --green-light: #3f7a2a;
    --yellow: #f4d21a;
    --gold: #d8b45a;
    --white: #ffffff;
    --title-ink: #2f5a1b;
  }
  * { margin: 0; padding: 0; box-sizing: border-box; }
  html, body { width: 851px; height: 1200px; overflow: hidden; background: #fff; }
  .flyer {
    position: relative; width: 851px; height: 1200px; overflow: hidden;
    background: linear-gradient(180deg, var(--green) 0%, var(--green-dark) 100%);
    font-family: "Open Sans", Arial, sans-serif;
  }
  .hero-photo {
    position: absolute; left: 0; top: 0; width: 851px; height: 220px;
    background: linear-gradient(160deg, #e8c46a 0%, #c99a3a 40%, #f0d58a 70%, #a9772a 100%);
  }
  .title-band {
    position: absolute; left: 0; top: 270px; width: 851px; height: 98px;
    background: var(--yellow);
    display: flex; align-items: center; justify-content: center;
  }
  .title-band h1 {
    font-family: "Anton", Impact, sans-serif; font-weight: 400;
    font-size: 84px; letter-spacing: 1px; color: var(--title-ink); line-height: 1;
  }
  .products { position: absolute; left: 38px; top: 395px; list-style: none; }
  .products li {
    color: var(--white); font-weight: 700; font-size: 25px;
    height: 68px; display: flex; align-items: center;
  }
  .products li::before {
    content: ""; width: 12px; height: 12px; border-radius: 50%;
    background: var(--yellow); margin-right: 18px; flex: none;
  }
  .potato-note {
    position: absolute; left: 60px; width: 731px; top: 735px;
    text-align: center; color: var(--yellow); font-weight: 700;
    font-size: 20px; line-height: 1.32;
  }
  .promises { position: absolute; left: 22px; top: 958px; list-style: none; }
  .promises li {
    color: var(--yellow); font-weight: 800; font-size: 24px;
    height: 36px; display: flex; align-items: center;
  }
  .promises li::before {
    content: ""; width: 9px; height: 9px; transform: rotate(45deg);
    background: var(--white); margin-right: 12px;
  }
  .offer {
    position: absolute; left: 470px; top: 950px; width: 370px; height: 180px;
    background: var(--white);
  }
  .offer-head {
    height: 46px; background: var(--green-light);
    display: flex; align-items: center; justify-content: space-between; padding: 0 14px 0 30px;
  }
  .offer-head .offer-label { color: var(--white); font-weight: 700; font-size: 18px; }
  .offer-head .offer-brand { color: var(--white); font-weight: 700; font-size: 13px; }
  .offer-amount {
    text-align: center; font-family: "Anton", Impact, sans-serif; font-size: 84px;
    color: var(--yellow); line-height: 1; margin-top: 4px;
  }
  .offer-terms {
    text-align: center; color: var(--green); font-weight: 800; font-size: 19px;
  }
  .brand {
    position: absolute; left: 22px; top: 1080px;
    font-weight: 700; font-size: 30px; color: var(--gold); letter-spacing: 1px;
  }
  .footer {
    position: absolute; left: 0; top: 1145px; width: 851px; height: 55px;
    background: var(--green-light);
    display: flex; align-items: center; padding-left: 22px;
    color: var(--white); font-weight: 600; font-size: 15.5px;
  }
</style>
</head>
<body>
<main class="flyer">
  <div class="hero-photo" role="img" aria-label="Close-up photograph of golden straw"></div>

  <header class="title-band"><h1>HAY, STRAW, HAYLAGE</h1></header>

  <ul class="products">
    <li>Meadow and Seed Hay Available in Small or Large Bales</li>
    <li>Haylage Available in Bale Size 1.2 x 0.8 x 0.7m/165-175kgs</li>
    <li>Oat and Wheat Straw Available in Small or Large Bales</li>
    <li>Barley Straw Available in Large Bales</li>
  </ul>

  <p class="potato-note">We also sell home grown white marfona and red Mozart potatoes!<br>Available in 12.5 and 25kg bags. Superb value for the money at £3<br>and £5 per bag!</p>

  <ul class="promises">
    <li>Delivery Available</li>
    <li>Consistent Quality</li>
    <li>Reliable Service</li>
  </ul>

  <section class="offer">
    <div class="offer-head">
      <span class="offer-label">Limited Time Offer!</span>
      <span class="offer-brand">BRACKENDALE FARM</span>
    </div>
    <div class="offer-amount">10% OFF</div>
    <div class="offer-terms">your first order with this leaflet</div>
  </section>

  <div class="brand">BRACKENDALE FARM</div>

  <footer class="footer">Farm Office: 01163 482705 &nbsp;·&nbsp; Mobile: 07938 254160, 07815 440372 &nbsp;·&nbsp; www.brackendalefarm.co.uk</footer>
</main>
</body>
</html>
```